Corvane Systems Modern, Sleek One Pager/Slick Sheet

Creative Brief: One-Pager Design for Corvane Systems
Project Overview:
We are seeking a highly skilled graphic designer to create a modern, sleek, and visually impactful one-pager (slick sheet) for Corvane Systems, a leading company in the defense and aerospace sector. This slick sheet will serve as a high-level marketing asset, designed to quickly capture attention and communicate Corvane Systems’s cutting-edge capabilities, technological expertise, and commitment to national security and innovation.
Key Objectives:
Establish a high-tech, sophisticated look and feel that aligns with the defense and aerospace industries.
Highlight Corvane Systems’s core competencies, key services, and differentiators with clear and concise messaging.
Ensure the design supports easy readability and quick scanning of critical information.
Incorporate strong visual hierarchy and premium, professional aesthetics.
Design Specifications:
Format: Single-page, print and digital distribution-ready (PDF format).
Layout Style: Clean, minimalist, and balanced with ample white space.
Typography: Modern, sans-serif fonts that convey innovation and strength.
Color Palette: Incorporate Corvane Systems’s brand colors (navy blue, steel gray, white, accents of metallic or deep reds if applicable).
Imagery: Use high-resolution imagery that reflects advanced technology, aerospace engineering, and national defense. Subtle technical graphics, schematics, or abstract patterns are acceptable to enhance visual interest without clutter.
Content Elements (To Be Provided):
Company Logo and Tagline
Key Capabilities and Service Offerings
Differentiators and Core Competencies
Contact Information
Visual Icons or Infographics for Quick Reference (if applicable)
Tone & Mood:
Professional, authoritative, and cutting-edge
Emphasizes trust, innovation, and mission-critical solutions
Appeals to government and defense industry stakeholders
Deliverables:
Final high-resolution print-ready PDF
Digital-friendly PDF optimized for email and web use
Source files (Adobe Illustrator, InDesign, or equivalent)
Target Market(s)
Defense/Aviation
Industry/Entity Type
Defense/Aviation
Look and feel

```html
<!DOCTYPE html>
<html lang="en">
<head>
<meta charset="utf-8">
<title>Corvane Systems – Capabilities Sheet</title>
<link href="https://fonts.googleapis.com/css2?family=Montserrat:wght@600;700;800&family=Mulish:wght@400;500&family=Oswald:wght@500;600&display=swap" rel="stylesheet">
<style>
  :root{
    --ink:#231f20;
    --steel:#6d6c6e;
    --paper:#ffffff;
    --copy:#4d4d4f;
    --sky-top:#5f86b8;
    --sky-low:#b9cbe0;
    --field:#5d6e3c;
    --tarmac:#8f8c86;
  }
  *{margin:0;padding:0;box-sizing:border-box}
  html,body{width:848px;height:1200px;overflow:hidden;background:var(--paper)}
  .sheet{position:relative;width:848px;height:1200px;overflow:hidden;font-family:"Mulish",sans-serif;color:var(--ink)}

  .hero{position:absolute;left:0;top:0;width:848px;height:283px;
    background:linear-gradient(180deg,var(--sky-top) 0%,var(--sky-low) 45%,var(--field) 50%,#6f7560 58%,var(--tarmac) 64%,#9a968f 100%)}
  .brand{position:absolute;left:26px;top:44px;display:flex;align-items:center;gap:12px}
  .brand-mark{width:30px;height:30px;background:var(--ink)}
  .brand-name{font-family:"Montserrat",sans-serif;font-weight:700;font-size:34px;letter-spacing:3px;color:var(--ink);text-transform:uppercase}

  .capabilities{position:absolute;left:0;top:283px;width:431px;height:252px;background:var(--ink);color:var(--paper)}
  .differentiators{position:absolute;left:431px;top:283px;width:417px;height:252px;background:var(--steel);color:var(--paper)}
  .panel-title{font-family:"Montserrat",sans-serif;font-weight:800;font-size:23.5px;line-height:30px;letter-spacing:.2px}
  .capabilities .panel-title{position:absolute;left:30px;top:26px}
  .differentiators .panel-title{position:absolute;left:32px;top:33px}
  .panel-copy{position:absolute;font-size:12.4px;line-height:14.8px}
  .capabilities .panel-copy{left:32px;top:66px;width:360px}
  .differentiators .panel-copy{left:36px;top:107px;width:360px}

  .offerings{position:absolute;left:0;top:535px;width:848px;height:540px;background:var(--paper)}
  .offerings-rail{position:absolute;left:0;top:0;width:105px;height:540px;background:var(--ink)}
  .offerings-title{position:absolute;left:29px;top:498px;transform-origin:0 0;transform:rotate(-90deg);
    font-family:"Oswald",sans-serif;font-weight:600;font-size:64px;line-height:50px;letter-spacing:.5px;color:var(--paper);white-space:nowrap}
  .notch{position:absolute;left:105px;width:0;height:0;border-top:9px solid transparent;border-bottom:9px solid transparent;border-left:9px solid var(--ink)}
  .service{position:absolute;left:130px;width:700px}
  .service-icon{position:absolute;left:0;top:0;width:65px;height:65px;border-radius:50%;background:var(--ink);display:flex;align-items:center;justify-content:center}
  .service-name{position:absolute;left:92px;top:-2px;font-family:"Montserrat",sans-serif;font-weight:600;font-size:19.5px;color:var(--ink);white-space:nowrap}
  .service-copy{position:absolute;left:90px;top:27px;width:600px;font-size:16.6px;line-height:20.5px;color:var(--copy)}

  .contact{position:absolute;left:0;top:1075px;width:848px;height:125px;background:var(--ink);color:var(--paper)}
  .contact-icon{position:absolute;top:30px;width:58px;height:58px;border-radius:50%;background:var(--paper);display:flex;align-items:center;justify-content:center}
  .contact-label{position:absolute;top:29px;font-family:"Montserrat",sans-serif;font-weight:600;font-size:19px;letter-spacing:.5px}
  .contact-value{position:absolute;top:54px;font-family:"Oswald",sans-serif;font-weight:500;font-size:30px;line-height:36px}
</style>
</head>
<body>
<main class="sheet">
  <header class="hero" role="img" aria-label="Photograph of a twin-turboprop aircraft and a tiltrotor parked on an airfield apron beside a hangar under a blue sky">
    <div class="brand">
      <span class="brand-mark"></span>
      <span class="brand-name">Corvane Systems</span>
    </div>
  </header>

  <section class="capabilities">
    <h2 class="panel-title">KEY CAPABILITIES</h2>
    <p class="panel-copy">Lorem ipsum dolor sit amet, consectetur adipiscing elit, sed do eiusmod tempor incididunt ut labore et dolore magna aliqua. Ut enim ad minim veniam, quis nostrud exercitation ullamco laboris nisi ut aliquip ex ea commodo consequat. Duis aute irure dolor in reprehenderit in voluptate velit esse cillum dolore eu fugiat nulla pariatur. Excepteur sint occaecat cupidatat non proident, sunt in culpa qui officia deserunt mollit anim id est l smod tempor incididunt ut labore et dolore magna aliqua. Ut enim ad minim veniam, quis nostrud exercitation ullamco laboris nisi ut aliquip ex ea commodo consequat. Duis aute irure dolor in reprehenderit</p>
  </section>

  <section class="differentiators">
    <h2 class="panel-title">DIFFERENTIATORS AND<br>CORE COMPETENCIES</h2>
    <p class="panel-copy">Lorem ipsum dolor sit amet, consectetur adipiscing elit, sed do eiusmod tempor incididunt ut labore et dolore magna aliqua. Ut enim ad minim veniam, quis nostrud exercitation ullamco laboris nisi ut aliquip ex ea commodo consequat. Duis aute irure dolor in reprehenderit in voluptate velit esse cillum dolore eu fugiat nulla pariatur. Excepteur sint occaecat cupidatat non proident, sunt in culpa qui officia deserunt mollit anim id est l</p>
  </section>

  <section class="offerings">
    <div class="offerings-rail"></div>
    <h2 class="offerings-title">SERVICE OFFERINGS</h2>
    <span class="notch" style="top:62px"></span>
    <span class="notch" style="top:155px"></span>
    <span class="notch" style="top:272px"></span>
    <span class="notch" style="top:369px"></span>
    <span class="notch" style="top:462px"></span>

    <article class="service" style="top:43px">
      <div class="service-icon">
        <svg width="40" height="40" viewBox="0 0 40 40" fill="none" stroke="#fff" stroke-width="3"><circle cx="18" cy="22" r="14"/><circle cx="18" cy="22" r="8"/><circle cx="18" cy="22" r="2.5" fill="#fff"/><path d="M18 22 L32 8" stroke-linecap="round"/><path d="M29 6 l5 0 0 5" stroke-width="2.5"/></svg>
      </div>
      <h3 class="service-name">ISR Special Mission</h3>
      <p class="service-copy">Global Intelligence, Surveillance, and Reconnaissance providing creative solutions in multi-domain operations</p>
    </article>

    <article class="service" style="top:138px">
      <div class="service-icon">
        <svg width="40" height="40" viewBox="0 0 40 40" fill="none" stroke="#fff" stroke-width="2.5"><path d="M12 24 a9 9 0 1 1 10 0 v4 h-10 z"/><path d="M12 31 h10 M13 34 h8"/><circle cx="17" cy="15" r="2" fill="#fff"/><path d="M19 15 L30 10 M19 16 L32 18 M18 17 L28 26" stroke-width="1.8"/><circle cx="31" cy="9.5" r="2" fill="#fff"/><circle cx="33" cy="18" r="2" fill="#fff"/><circle cx="29" cy="27" r="2" fill="#fff"/></svg>
      </div>
      <h3 class="service-name">Research and Development</h3>
      <p class="service-copy">Specialize in testing of new technologies for future ISR construct, next-generation warfighting capabilities</p>
    </article>

    <article class="service" style="top:249px">
      <div class="service-icon">
        <svg width="38" height="38" viewBox="0 0 38 38" fill="#fff"><path d="M19 4 L35 12 H3 Z"/><rect x="4" y="14" width="30" height="2.5"/><rect x="7" y="18" width="4" height="11"/><rect x="14" y="18" width="4" height="11"/><rect x="21" y="18" width="4" height="11"/><rect x="28" y="18" width="4" height="11"/><rect x="4" y="30" width="30" height="3"/></svg>
      </div>
      <h3 class="service-name">CONUS Efforts</h3>
      <p class="service-copy">State/Federal Law Enforcement, Natural Disaster, Search and Rescue, Specialized SOF programs</p>
    </article>

    <article class="service" style="top:346px">
      <div class="service-icon">
        <svg width="42" height="42" viewBox="0 0 42 42" fill="none" stroke="#fff" stroke-width="3" stroke-linecap="round" stroke-linejoin="round"><path d="M4 14 L12 8 L20 12 L28 8 L38 14"/><path d="M10 12 L26 26 a2.5 2.5 0 0 1 -3.5 3.5 L18 25"/><path d="M22.5 29.5 a2.5 2.5 0 0 1 -3.5 3.5 L15 29"/><path d="M19 33 a2.5 2.5 0 0 1 -3.5 3.5 L12 33"/><path d="M20 12 L15 17 a2.5 2.5 0 0 0 3.5 3.5 L23 16 L32 24"/></svg>
      </div>
      <h3 class="service-name">OCONUS Efforts</h3>
      <p class="service-copy">Streamlining international collaboration to shape the global landscape and safeguarding our nation and allies</p>
    </article>

    <article class="service" style="top:439px">
      <div class="service-icon">
        <svg width="40" height="40" viewBox="0 0 40 40" fill="#fff"><path d="M31 6 a3 3 0 0 1 3 3 L26 17 L30 31 L27 34 L21 22 L15 28 L16 33 L13 35 L11 29 L5 27 L7 24 L12 25 L18 19 L6 13 L9 10 L23 14 Z"/><path d="M4 36 L10 30" stroke="#fff" stroke-width="2"/></svg>
      </div>
      <h3 class="service-name">Aviation Training</h3>
      <p class="service-copy">Solving complex problems with dynamic solutions for future warfighters</p>
    </article>
  </section>

  <footer class="contact">
    <div class="contact-icon" style="left:108px">
      <svg width="26" height="26" viewBox="0 0 24 24" fill="#231f20"><path d="M6.6 10.8a15 15 0 0 0 6.6 6.6l2.2-2.2c.3-.3.7-.4 1-.2 1.1.4 2.3.6 3.6.6.6 0 1 .4 1 1V20c0 .6-.4 1-1 1A17 17 0 0 1 3 4c0-.6.4-1 1-1h3.5c.6 0 1 .4 1 1 0 1.3.2 2.5.6 3.6.1.3 0 .7-.2 1z"/></svg>
    </div>
    <span class="contact-label" style="left:194px">CALL US</span>
    <span class="contact-value" style="left:190px">(555) 014-2287</span>

    <div class="contact-icon" style="left:421px">
      <svg width="30" height="22" viewBox="0 0 30 22" fill="none" stroke="#231f20" stroke-width="2.2"><rect x="1.5" y="1.5" width="27" height="19"/><path d="M1.5 1.5 L15 12 L28.5 1.5 M1.5 20.5 L11 10.5 M28.5 20.5 L19 10.5"/></svg>
    </div>
    <span class="contact-label" style="left:505px">EMAIL US</span>
    <span class="contact-value" style="left:500px;font-size:28px">info@corvanesystems.com</span>
  </footer>
</main>
</body>
</html>
```